Criminal Defense Law Firm needs Stationary design Theme for a Business Card, Envelope, and Letterhea

Our Law Firm is seeking a general design concept for a business card, letterhead, and Envelope.

Our website is WillowcrestTrialDesk.com

A design for these three items is requested to keep branding in place for the firm. Would like to keep the Firm Colors on the website consistent with our branding on business cards, letterheads, and mailing envelopes #10 size to be exact.

We would like business cards printed front and back with Law firm Colors from website.

Letterhead with law firm colors as well. Design is not limited to just the header, but the footer can be utilized as well for email, website, phone, fax, etc.

Simple #10 envelope consisting of the same design principles set out in the previous two designs.

```html
<!DOCTYPE html>
<html lang="en">
<head>
<meta charset="utf-8">
<title>Willowcrest Trial Offices – Stationery</title>
<link rel="stylesheet" href="https://fonts.googleapis.com/css2?family=Spectral:wght@400&family=PT+Sans:wght@400;700&family=Dancing+Script:wght@400&display=swap">
<style>
:root{
  --cyan:#12aecf;
  --gold:#b0925a;
  --ink:#3a3a3a;
  --muted:#555;
  --paper:#ffffff;
  --backdrop:#ececec;
  --watermark:#f2f2f2;
  --window:#e6e6e6;
  --serif:"Spectral", Georgia, serif;
  --sans:"PT Sans", Arial, sans-serif;
  --script:"Dancing Script", cursive;
}
*{box-sizing:border-box;margin:0;padding:0}
html,body{width:1200px;height:765px;overflow:hidden}
body{background:var(--backdrop);font-family:var(--sans);color:var(--ink);position:relative}
.piece{position:absolute;background:var(--paper);overflow:hidden;box-shadow:0 1px 3px rgba(0,0,0,.12)}
.abs{position:absolute}
.brand{position:absolute;display:flex;align-items:center}
.brand-mark{border:1.5px solid var(--ink);border-radius:50%;flex:none}
.brand-name{font-family:var(--serif);text-transform:uppercase;letter-spacing:.06em;line-height:1.1;color:var(--ink);font-weight:400}
.bands{position:absolute;left:0;right:0;bottom:0;display:flex}
.bands .cyan{background:var(--cyan);flex:1}
.bands .gold{background:var(--gold);flex:1}
.web{font-size:8px;color:var(--muted)}
.web b{font-weight:400;color:var(--cyan)}
.contact{list-style:none}
.contact li{display:flex;align-items:center;gap:3px}
.contact svg{flex:none}
.watermark{position:absolute;border-radius:50%;border:12px solid var(--watermark)}

/* Letterhead */
.letterhead{left:99px;top:33px;width:488px;height:688px}
.letterhead .brand{left:45px;top:53px;gap:10px}
.letterhead .brand-mark{width:37px;height:37px}
.letterhead .brand-name{font-size:14px}
.letterhead .watermark{left:3px;top:138px;width:378px;height:378px}
.letter{position:absolute;left:46px;top:157px;width:390px}
.letter .date{font-size:11px;color:var(--muted)}
.letter .greet{font-size:11.5px;color:var(--muted);margin-top:7px}
.letter p{font-size:8.3px;line-height:10.6px;color:var(--muted);margin-top:10px}
.letter .greet + p{margin-top:8px}
.signature{position:absolute;left:46px;top:500px}
.signature .sig{font-family:var(--script);font-size:17px;color:var(--muted)}
.signature .role{font-size:8px;font-weight:700;color:var(--muted);margin-top:1px}
.letterhead .address{left:46px;top:598px;font-size:8.3px;line-height:10.5px;color:var(--muted)}
.letterhead .contact{left:46px;top:627px;font-size:8.3px;line-height:10.5px;color:var(--muted)}
.letterhead .web{right:30px;top:644px;font-size:8.3px}
.letterhead .bands{height:10px}

/* Envelope back */
.envelope-back{left:620px;top:64px;width:537px;height:233px}
.envelope-back .flap{position:absolute;left:0;top:0}
.envelope-back .flap-name{left:0;right:0;top:20px;text-align:center;font-family:var(--serif);font-size:12px;letter-spacing:.08em;text-transform:uppercase;color:var(--ink)}
.envelope-back .web{left:0;right:0;top:213px;text-align:center;font-size:7.5px}

/* Envelope front */
.envelope-front{left:620px;top:340px;width:548px;height:236px}
.envelope-front .brand{left:39px;top:39px;gap:9px}
.envelope-front .brand-mark{width:30px;height:30px}
.envelope-front .brand-name{font-size:11px}
.envelope-front .address{left:378px;top:35px;font-size:7.4px;line-height:8.4px;color:var(--muted)}
.envelope-front .contact{left:378px;top:61px;font-size:7.4px;line-height:8.4px;color:var(--muted)}
.envelope-front .window{left:38px;top:112px;width:189px;height:48px;border:1.5px solid #c9c9c9;border-radius:7px;background:linear-gradient(90deg,var(--window),#f7f7f7)}
.envelope-front .web{left:0;width:558px;top:207px;text-align:center;font-size:8px}
.envelope-front .bands{height:10px}

/* Business card front */
.card-front{left:620px;top:597px;width:222px;height:126px}
.card-front .brand{left:40px;top:24px;gap:7px}
.card-front .brand-mark{width:24px;height:24px}
.card-front .brand-name{font-size:8.6px}
.card-front .person{left:15px;top:69px}
.card-front .person .name{font-size:6.6px;font-weight:700;color:var(--gold);letter-spacing:.03em}
.card-front .person .title{font-size:5.3px;color:var(--cyan);margin-top:1px}
.card-front .contact{left:15px;top:89px;font-size:4.4px;line-height:6.4px;color:var(--muted)}
.card-front .address{left:133px;top:88px;font-size:4.4px;line-height:6.4px;color:var(--muted)}
.card-front .web{left:133px;top:101px;font-size:4.4px}
.card-front .bands{height:7px}

/* Business card back */
.card-back{left:860px;top:597px;width:222px;height:124px;background:var(--cyan)}
.card-back .watermark{left:49px;top:0;width:90px;height:90px;border:6px solid rgba(255,255,255,.12)}
.card-back .brand{left:38px;top:50px;gap:7px}
.card-back .brand-mark{width:24px;height:24px;border-color:#fff}
.card-back .brand-name{font-size:8.6px;color:#fff}
.card-back .web{left:0;right:0;top:112px;text-align:center;font-size:5px;color:#fff}
</style>
</head>
<body>

<!-- Letterhead -->
<section class="piece letterhead" aria-label="Letterhead">
  <div class="watermark"></div>
  <div class="brand">
    <span class="brand-mark"></span>
    <span class="brand-name">Willowcrest Trial<br>Law Offices</span>
  </div>
  <div class="letter">
    <div class="date">May/09/2014</div>
    <div class="greet">Dear Daniel,</div>
    <p>Lorem Ipsum is simply dummy text of the printing and typesetting industry. Lorem Ipsum has been the industry's standard dummy text ever since the 1500s, when an unknown printer took a galley of type and scrambled it to make a type specimen book. It has survived not only five centuries, but also the leap into electronic typesetting, remaining essentially unchanged. It was popularised in the 1960s with the release of Typeline sheets containing Lorem Ipsum passages, and more recently with desktop publishing software like PageForge including versions of Lorem Ipsum.</p>
    <p>Contrary to popular belief, Lorem Ipsum is not simply random text. It has roots in a piece of classical Latin literature from 45 BC, making it over 2000 years old. Richard Alcott, a Latin professor at Briarfield College in Virginia, looked up one of the more obscure Latin words, consectetur, from a Lorem Ipsum passage, and going through the cites of the word in classical literature, discovered the undoubtable source. Lorem Ipsum comes from sections 1.10.32 and 1.10.33 of "de Finibus Bonorum et Malorum" (The Extremes of Good and Evil) by Marcus Vell, written in 45 BC. This book is a treatise on the theory of ethics, very popular during the Renaissance. The first line of Lorem Ipsum, "Lorem ipsum dolor sit amet..", comes from a line in section 1.10.32.</p>
    <p>The standard chunk of Lorem Ipsum used since the 1500s is reproduced below for those interested. Sections 1.10.32 and 1.10.33 from "de Finibus Bonorum et Malorum" by Marcus Vell are also reproduced in their exact original form, accompanied by English versions from the 1914 translation by H. Renwick.</p>
    <p>It is a long established fact that a reader will be distracted by the readable content of a page when looking at its layout. The point of using Lorem Ipsum is that it has a more-or-less normal distribution of letters, as opposed to using 'Content here, content here', making it look like readable English. Many desktop publishing packages and web page editors now use Lorem Ipsum as their default model text, and a search for 'lorem ipsum' will uncover many web sites still in their infancy. Various versions have evolved over the years, sometimes by accident, sometimes on purpose (injected humour and the like).</p>
  </div>
  <div class="signature">
    <div class="sig">Marcus Ellery</div>
    <div class="role">Company Director</div>
  </div>
  <address class="abs address" style="font-style:normal">412 Larkmoor Avenue,<br>Fernhollow, NM 87000</address>
  <ul class="abs contact">
    <li><svg width="7" height="7" viewBox="0 0 10 10"><path d="M2 1l2 2-1 1.5c.6 1.2 1.3 1.9 2.5 2.5L7 6l2 2-1.5 1.5C4.5 9 1 5.5.5 2.5z" fill="var(--gold)"/></svg>555.014.2290</li>
    <li><svg width="7" height="7" viewBox="0 0 10 10"><path d="M2 1l2 2-1 1.5c.6 1.2 1.3 1.9 2.5 2.5L7 6l2 2-1.5 1.5C4.5 9 1 5.5.5 2.5z" fill="var(--gold)"/></svg>555.014.7731</li>
    <li><svg width="7" height="7" viewBox="0 0 10 10"><rect x=".5" y="2" width="9" height="6" fill="var(--gold)"/><path d="M.5 2l4.5 3.5L9.5 2" stroke="#fff" fill="none"/></svg>name@<span style="color:var(--cyan)">WillowcrestTrialDesk</span>.com</li>
  </ul>
  <div class="abs web">www.<b>WillowcrestTrialDesk</b>.com</div>
  <div class="bands"><span class="cyan"></span><span class="gold"></span></div>
</section>

<!-- Envelope back -->
<section class="piece envelope-back" aria-label="Envelope back">
  <svg class="flap" width="537" height="233" viewBox="0 0 537 233">
    <path d="M0 0H537L505 60Q499 64 490 64H47Q38 64 32 60Z" fill="#fbfbfb" stroke="#e4e4e4"/>
    <path d="M38 54H269V64H47Q41 64 38 59Z" fill="var(--cyan)"/>
    <path d="M269 54H499Q496 64 490 64H269Z" fill="var(--gold)"/>
  </svg>
  <div class="abs flap-name">Willowcrest Trial</div>
  <div class="abs web">www.<b>WillowcrestTrialDesk</b>.com</div>
</section>

<!-- Envelope front -->
<section class="piece envelope-front" aria-label="Envelope front">
  <div class="brand">
    <span class="brand-mark"></span>
    <span class="brand-name">Willowcrest Trial<br>Law Offices</span>
  </div>
  <address class="abs address" style="font-style:normal">412 Larkmoor Avenue,<br>Fernhollow, NM 87000</address>
  <ul class="abs contact">
    <li><svg width="6" height="6" viewBox="0 0 10 10"><path d="M2 1l2 2-1 1.5c.6 1.2 1.3 1.9 2.5 2.5L7 6l2 2-1.5 1.5C4.5 9 1 5.5.5 2.5z" fill="var(--gold)"/></svg>555.014.2290</li>
    <li><svg width="6" height="6" viewBox="0 0 10 10"><path d="M2 1l2 2-1 1.5c.6 1.2 1.3 1.9 2.5 2.5L7 6l2 2-1.5 1.5C4.5 9 1 5.5.5 2.5z" fill="var(--gold)"/></svg>555.014.7731</li>
    <li><svg width="6" height="6" viewBox="0 0 10 10"><rect x=".5" y="2" width="9" height="6" fill="var(--gold)"/><path d="M.5 2l4.5 3.5L9.5 2" stroke="#fff" fill="none"/></svg>name@<span style="color:var(--cyan)">WillowcrestTrialDesk</span>.com</li>
  </ul>
  <div class="abs window"></div>
  <div class="abs web">www.<b>WillowcrestTrialDesk</b>.com</div>
  <div class="bands"><span class="cyan"></span><span class="gold"></span></div>
</section>

<!-- Business card front -->
<section class="piece card-front" aria-label="Business card front">
  <div class="brand">
    <span class="brand-mark"></span>
    <span class="brand-name">Willowcrest Trial<br>Law Offices</span>
  </div>
  <div class="abs person">
    <div class="name">MARCUS ELLERY</div>
    <div class="title">Lawyer</div>
  </div>
  <ul class="abs contact">
    <li><svg width="4" height="4" viewBox="0 0 10 10"><circle cx="5" cy="5" r="5" fill="var(--gold)"/></svg>555.014.2290</li>
    <li><svg width="4" height="4" viewBox="0 0 10 10"><circle cx="5" cy="5" r="5" fill="var(--gold)"/></svg>555.014.7731</li>
    <li><svg width="4" height="4" viewBox="0 0 10 10"><circle cx="5" cy="5" r="5" fill="var(--gold)"/></svg>name@<span style="color:var(--cyan)">WillowcrestTrialDesk</span>.com</li>
  </ul>
  <address class="abs address" style="font-style:normal">412 Larkmoor Avenue,<br>Fernhollow, NM 87000</address>
  <div class="abs web">www.<b>WillowcrestTrialDesk</b>.com</div>
  <div class="bands"><span class="cyan"></span><span class="gold"></span></div>
</section>

<!-- Business card back -->
<section class="piece card-back" aria-label="Business card back">
  <div class="watermark"></div>
  <div class="brand">
    <span class="brand-mark"></span>
    <span class="brand-name">Willowcrest Trial<br>Law Offices</span>
  </div>
  <div class="abs web">www.WillowcrestTrialDesk.com</div>
</section>

</body>
</html>
```